Stationery design for pet company

We need a designer for stationery designs. The name of our company is Plimarv. We specialise in pet accessories as well as distribution of pet food. We also have a brand under us for our website called Tailwaggroove. We will need a letterhead for Plimarv and another for Tailwaggroove with matching envelopes. We also would like to have a business card design with name, contact details etc with the Plimarv logo on one side of the card. The other side of the business card should have the full logo of Tailwaggroove with our website www.tailwaggroove.example.

Target Market(s)

Stationery for Plimarv is for retail shops and suppliers, therefore should have a more professional feel. Stationery for Tailwaggroove is mainly for customers from the website.

Industry/Entity Type

Business

Requirements
Must have
• Preferably a use of black colour for the business card.
Nice to have
• Professional feel
Should not have
• Childish designs

```html
<!DOCTYPE html>
<html lang="en">
<head>
<meta charset="utf-8">
<title>Plimarv Business Card</title>
<link rel="stylesheet" href="https://fonts.googleapis.com/css2?family=Lato:wght@400;700;900&display=swap">
<style>
  :root {
    --backdrop: #e4e5e7;
    --card-white: #ffffff;
    --ink: #1e1e1e;
    --ink-soft: #444444;
    --gold: #c9a04f;
    --gold-light: #d2a753;
    --gold-dark: #8f7134;
    --rule: #2a2a2a;
    --wordmark: #5b2d8a;
    --mascot: #2b2b2b;
  }
  * { margin: 0; padding: 0; box-sizing: border-box; }
  html, body {
    width: 1200px; height: 1200px; overflow: hidden;
    background: var(--backdrop);
    font-family: "Lato", sans-serif;
  }
  .canvas { position: relative; width: 1200px; height: 1200px; }

  .card {
    position: absolute; left: 280px; width: 640px; height: 365px;
    border-radius: 18px; overflow: hidden;
    box-shadow: 0 4px 14px rgba(0,0,0,0.18);
  }

  /* Front */
  .card-front {
    top: 211px;
    background: linear-gradient(160deg, var(--card-white) 70%, #e9e9ec 100%);
  }
  .brand-block {
    position: absolute; left: 0; top: 108px; width: 290px;
    display: flex; flex-direction: column; align-items: center; gap: 14px;
  }
  .brand-dot {
    width: 62px; height: 62px; border-radius: 50%; background: var(--gold);
  }
  .brand-name {
    font-weight: 700; font-size: 32px; letter-spacing: 3px; color: var(--ink); line-height: 34px;
  }
  .divider {
    position: absolute; left: 263px; top: 48px; width: 14px; height: 242px;
    background: linear-gradient(90deg, rgba(0,0,0,0.12), rgba(0,0,0,0));
    border-left: 1px solid rgba(0,0,0,0.08);
  }
  .details {
    position: absolute; left: 301px; top: 44px; color: var(--ink-soft);
    font-size: 15px; line-height: 21px;
  }
  .person-name { font-weight: 900; font-size: 20px; color: var(--ink); line-height: 24px; }
  .company-name { font-weight: 900; font-size: 16px; color: var(--ink); margin-top: 47px; }
  .contact-group { margin-top: 35px; }
  .line { display: flex; align-items: center; gap: 6px; }
  .line svg { flex: none; }
  .front-rule {
    position: absolute; left: 0; right: 0; top: 324px; height: 3px; background: var(--rule);
  }
  .front-band {
    position: absolute; left: 0; right: 0; top: 329px; bottom: 0;
    background: linear-gradient(90deg, var(--gold-light), var(--gold) 55%, var(--gold-dark));
  }

  /* Back */
  .card-back {
    top: 625px;
    background: linear-gradient(180deg, var(--gold-light) 0%, var(--gold) 50%, var(--gold-dark) 100%);
  }
  .mascot-area {
    position: absolute; left: 262px; top: 91px; width: 112px; height: 107px;
    border-radius: 10px;
    background: linear-gradient(180deg, var(--mascot), #3a2a2a);
  }
  .back-wordmark {
    position: absolute; left: 0; right: 0; top: 198px; text-align: center;
    font-weight: 700; font-size: 48px; line-height: 60px; color: var(--wordmark);
  }
  .back-url {
    position: absolute; left: 0; right: 0; top: 318px; text-align: center;
    color: #ffffff; font-weight: 700; font-size: 17px; letter-spacing: 3px;
  }
</style>
</head>
<body>
<main class="canvas">
  <section class="card card-front">
    <div class="brand-block">
      <span class="brand-dot"></span>
      <span class="brand-name">PLIMARV</span>
    </div>
    <div class="divider"></div>
    <div class="details">
      <p class="person-name">YOUR NAME</p>
      <p>Position</p>
      <p class="line">
        <svg width="10" height="16" viewBox="0 0 10 16"><rect x="1" y="1" width="8" height="14" rx="1.5" fill="none" stroke="#c9a04f" stroke-width="1.5"/><rect x="3" y="3" width="4" height="7" fill="#c9a04f"/></svg>
        +44(0)7700900123
      </p>
      <p class="company-name">PLIMARV</p>
      <p>123, Your Street,</p>
      <p>Your City, Country, 123.</p>
      <div class="contact-group">
        <p class="line">
          <svg width="16" height="13" viewBox="0 0 16 13"><path d="M1 4 Q8 -1 15 4 L13 6 L11 4 L5 4 L3 6 Z" fill="#c9a04f"/><rect x="3" y="6" width="10" height="6" rx="1" fill="#c9a04f"/></svg>
          +44(0)161 496 0742
        </p>
        <p class="line">
          <svg width="16" height="12" viewBox="0 0 16 12"><rect x="1" y="1" width="14" height="10" fill="none" stroke="#c9a04f" stroke-width="1.5"/><path d="M1 1 L8 7 L15 1" fill="none" stroke="#c9a04f" stroke-width="1.5"/></svg>
          enquiries@plimarv.example
        </p>
      </div>
    </div>
    <div class="front-rule"></div>
    <div class="front-band"></div>
  </section>

  <section class="card card-back">
    <div class="mascot-area" role="img" aria-label="Illustration of a dog mascot wearing a red cape"></div>
    <p class="back-wordmark">Tailwaggroove</p>
    <p class="back-url">www.tailwaggroove.example</p>
  </section>
</main>
</body>
</html>
```